July 2014 Larkhaven Marketing

Larkhaven Christian Day Schools provide the very best of what you want for your early learner....creative and challenging learning programs, experienced, nurturing teachers with high expectations, spacious, colorful classrooms and exciting opportunities for sharing with family members and the community. We need a postcard design to build enrollment.

Target Market(s)

Parents of children ages 0 to 8

Industry/Entity Type

Marketing

```html
<!DOCTYPE html>
<html lang="en">
<head>
<meta charset="utf-8">
<title>Larkhaven Christian Day Schools – Enrol Now Postcard</title>
<link rel="stylesheet" href="https://fonts.googleapis.com/css2?family=Fredoka:wght@600&display=swap">
<style>
  :root {
    --sky: #2ec3e7;
    --sky-soft: #bfeaf6;
    --white: #ffffff;
    --star: #ffe816;
  }
  html, body {
    margin: 0;
    padding: 0;
    width: 1200px;
    height: 932px;
    overflow: hidden;
    background: var(--white);
  }
  .postcard {
    position: relative;
    width: 1200px;
    height: 932px;
    overflow: hidden;
    background: var(--white);
    font-family: "Fredoka", "Varela Round", sans-serif;
    font-weight: 600;
    color: var(--white);
  }
  .diagonal-panel {
    position: absolute;
    inset: 0;
    width: 1200px;
    height: 932px;
  }
  .school-name {
    position: absolute;
    left: 74px;
    top: 50px;
    margin: 0;
    font-size: 79px;
    line-height: 82px;
    font-weight: 600;
    letter-spacing: 0.5px;
  }
  .highlights {
    position: absolute;
    left: 78px;
    top: 442px;
    margin: 0;
    padding: 0;
    list-style: none;
    font-size: 58px;
    line-height: 60px;
  }
  .highlights li {
    position: relative;
    padding-left: 72px;
  }
  .highlights .star {
    position: absolute;
    left: 0;
    top: 12px;
    width: 44px;
    height: 42px;
  }
  .child-illustration {
    position: absolute;
    left: 765px;
    top: 28px;
    width: 380px;
    height: 410px;
    border-radius: 48% 52% 45% 50%;
    background: radial-gradient(circle at 55% 45%, var(--white) 0%, var(--sky-soft) 100%);
  }
  .enrol-badge {
    position: absolute;
    left: 686px;
    top: 476px;
    width: 392px;
    height: 392px;
  }
  .enrol-badge svg {
    width: 100%;
    height: 100%;
  }
  .enrol-text {
    position: absolute;
    inset: 0;
    display: flex;
    align-items: center;
    justify-content: center;
    text-align: center;
    font-size: 86px;
    line-height: 92px;
    letter-spacing: 2px;
    transform: rotate(-6deg);
    color: var(--white);
  }
</style>
</head>
<body>
<main class="postcard">
  <svg class="diagonal-panel" viewBox="0 0 1200 932" aria-hidden="true">
    <polygon points="0,0 762,0 494,932 0,932" fill="var(--sky)"/>
  </svg>

  <h1 class="school-name">Larkhaven<br>Christian<br>Day Schools</h1>

  <ul class="highlights">
    <li><svg class="star" viewBox="0 0 24 23" aria-hidden="true"><polygon points="12,0 15,8.3 24,8.8 17,14.4 19.4,23 12,18 4.6,23 7,14.4 0,8.8 9,8.3" fill="var(--star)"/></svg>Creative</li>
    <li><svg class="star" viewBox="0 0 24 23" aria-hidden="true"><polygon points="12,0 15,8.3 24,8.8 17,14.4 19.4,23 12,18 4.6,23 7,14.4 0,8.8 9,8.3" fill="var(--star)"/></svg>Challenging</li>
    <li><svg class="star" viewBox="0 0 24 23" aria-hidden="true"><polygon points="12,0 15,8.3 24,8.8 17,14.4 19.4,23 12,18 4.6,23 7,14.4 0,8.8 9,8.3" fill="var(--star)"/></svg>Spacious</li>
    <li><svg class="star" viewBox="0 0 24 23" aria-hidden="true"><polygon points="12,0 15,8.3 24,8.8 17,14.4 19.4,23 12,18 4.6,23 7,14.4 0,8.8 9,8.3" fill="var(--star)"/></svg>Exciting</li>
    <li><svg class="star" viewBox="0 0 24 23" aria-hidden="true"><polygon points="12,0 15,8.3 24,8.8 17,14.4 19.4,23 12,18 4.6,23 7,14.4 0,8.8 9,8.3" fill="var(--star)"/></svg>Nurturing<br>Teachers</li>
  </ul>

  <div class="child-illustration" role="img" aria-label="Line illustration of a smiling young child's head in sky blue outline"></div>

  <div class="enrol-badge">
    <svg viewBox="0 0 400 400" aria-hidden="true">
      <defs>
        <path id="spike" d="M200,3 L214,28 L186,28 Z"/>
      </defs>
      <g fill="var(--sky)">
        <circle cx="200" cy="200" r="174"/>
        <use href="#spike" transform="rotate(0 200 200)"/>
        <use href="#spike" transform="rotate(9 200 200)"/>
        <use href="#spike" transform="rotate(18 200 200)"/>
        <use href="#spike" transform="rotate(27 200 200)"/>
        <use href="#spike" transform="rotate(36 200 200)"/>
        <use href="#spike" transform="rotate(45 200 200)"/>
        <use href="#spike" transform="rotate(54 200 200)"/>
        <use href="#spike" transform="rotate(63 200 200)"/>
        <use href="#spike" transform="rotate(72 200 200)"/>
        <use href="#spike" transform="rotate(81 200 200)"/>
        <use href="#spike" transform="rotate(90 200 200)"/>
        <use href="#spike" transform="rotate(99 200 200)"/>
        <use href="#spike" transform="rotate(108 200 200)"/>
        <use href="#spike" transform="rotate(117 200 200)"/>
        <use href="#spike" transform="rotate(126 200 200)"/>
        <use href="#spike" transform="rotate(135 200 200)"/>
        <use href="#spike" transform="rotate(144 200 200)"/>
        <use href="#spike" transform="rotate(153 200 200)"/>
        <use href="#spike" transform="rotate(162 200 200)"/>
        <use href="#spike" transform="rotate(171 200 200)"/>
        <use href="#spike" transform="rotate(180 200 200)"/>
        <use href="#spike" transform="rotate(189 200 200)"/>
        <use href="#spike" transform="rotate(198 200 200)"/>
        <use href="#spike" transform="rotate(207 200 200)"/>
        <use href="#spike" transform="rotate(216 200 200)"/>
        <use href="#spike" transform="rotate(225 200 200)"/>
        <use href="#spike" transform="rotate(234 200 200)"/>
        <use href="#spike" transform="rotate(243 200 200)"/>
        <use href="#spike" transform="rotate(252 200 200)"/>
        <use href="#spike" transform="rotate(261 200 200)"/>
        <use href="#spike" transform="rotate(270 200 200)"/>
        <use href="#spike" transform="rotate(279 200 200)"/>
        <use href="#spike" transform="rotate(288 200 200)"/>
        <use href="#spike" transform="rotate(297 200 200)"/>
        <use href="#spike" transform="rotate(306 200 200)"/>
        <use href="#spike" transform="rotate(315 200 200)"/>
        <use href="#spike" transform="rotate(324 200 200)"/>
        <use href="#spike" transform="rotate(333 200 200)"/>
        <use href="#spike" transform="rotate(342 200 200)"/>
        <use href="#spike" transform="rotate(351 200 200)"/>
      </g>
    </svg>
    <p class="enrol-text">ENROL<br>NOW!</p>
  </div>
</main>
</body>
</html>
```